stationary for hygienic company

We need a stationary design for hygienic company which provides public high end sanitary products and high end public lavatory.
We need a fresh and clean style stationary
we want the following things:
* logo (redesigned in eps/vector)
* Letterhead (with company details)
* letterhead (without company details)
* Business card
* note block
* ballpoint
* etcetera (a complete package)

```html
<!DOCTYPE html>
<html lang="en">
<head>
<meta charset="utf-8">
<title>Velmora Business Card</title>
<link href="https://fonts.googleapis.com/css2?family=Montserrat:wght@400;500;700&display=swap" rel="stylesheet">
<style>
  :root {
    --magenta: #e6007e;
    --navy: #1d1d8f;
    --cyan: #0aa9e9;
    --ink: #2b2b2b;
    --muted: #6f6f6f;
    --paper: #ffffff;
    --backdrop: #e9e9eb;
  }
  * { margin: 0; padding: 0; box-sizing: border-box; }
  html, body {
    width: 1200px; height: 960px; overflow: hidden;
    background: var(--backdrop);
    font-family: "Montserrat", Arial, sans-serif;
    color: var(--ink);
  }
  .sheet {
    position: relative; width: 1200px; height: 960px;
    display: flex; flex-direction: column; align-items: center;
    justify-content: center; gap: 60px;
  }
  .card {
    position: relative; width: 680px; height: 400px;
    background: var(--paper);
    box-shadow: 0 10px 30px rgba(0,0,0,0.12);
  }

  /* contact side */
  .brand-mark {
    position: absolute; left: 44px; top: 44px;
    display: flex; align-items: center; gap: 12px;
    font-size: 30px; font-weight: 700; color: var(--navy);
  }
  .brand-mark .dot {
    width: 22px; height: 22px; border-radius: 50%; background: var(--magenta);
  }
  .holder { position: absolute; right: 44px; top: 36px; text-align: right; }
  .holder-name { font-size: 21px; font-weight: 700; letter-spacing: 0.3px; }
  .holder-role { font-size: 13px; color: var(--muted); margin-top: 4px; }

  .company { position: absolute; left: 44px; bottom: 34px; }
  .company-name {
    font-size: 13px; font-weight: 500; letter-spacing: 1.6px;
    color: var(--muted); text-transform: uppercase; margin-bottom: 6px;
  }
  .company-line { font-size: 18px; line-height: 30px; display: flex; align-items: center; gap: 6px; }
  .company-line svg { width: 16px; height: 16px; flex: none; }

  .website {
    position: absolute; right: 44px; bottom: 40px;
    font-size: 17px; color: var(--ink);
  }
  .colour-bar {
    position: absolute; right: 0; bottom: 16px;
    display: flex; width: 200px; height: 12px;
  }
  .colour-bar span { flex: 1; }
  .colour-bar .magenta { background: var(--magenta); }
  .colour-bar .navy { background: var(--navy); }
  .colour-bar .cyan { background: var(--cyan); }

  /* brand side */
  .card-front {
    display: flex; align-items: center; justify-content: center;
  }
  .front-mark {
    display: flex; align-items: center; gap: 18px;
    font-size: 72px; font-weight: 500; color: var(--ink); letter-spacing: 1px;
  }
  .front-mark .dot {
    width: 40px; height: 40px; border-radius: 50%; background: var(--cyan);
  }
</style>
</head>
<body>
<main class="sheet">
  <section class="card card-contact">
    <div class="brand-mark"><span class="dot"></span>Velmora</div>
    <div class="holder">
      <p class="holder-name">Lukas Brenner</p>
      <p class="holder-role">Geschäftsführer</p>
    </div>
    <div class="company">
      <p class="company-name">Velmora Boutique Hygienique</p>
      <p class="company-line">51200 Tiranef, Morocco</p>
      <p class="company-line">
        <svg viewBox="0 0 16 16" aria-hidden="true"><rect x="1.5" y="3.5" width="13" height="9" fill="none" stroke="#555" stroke-width="1.2"/><path d="M1.5 3.5 L8 9 L14.5 3.5" fill="none" stroke="#555" stroke-width="1.2"/></svg>
        info@velmora.ma
      </p>
      <p class="company-line">
        <svg viewBox="0 0 16 16" aria-hidden="true"><rect x="2" y="2" width="12" height="12" rx="1.5" fill="none" stroke="#555" stroke-width="1.2"/><rect x="4.5" y="4" width="3" height="8" fill="#555"/><path d="M9.5 5h3M9.5 8h3M9.5 11h3" stroke="#555" stroke-width="1"/></svg>
        +212 661-204318
      </p>
    </div>
    <p class="website">www.velmora.ma</p>
    <div class="colour-bar"><span class="magenta"></span><span class="navy"></span><span class="cyan"></span></div>
  </section>

  <section class="card card-front">
    <div class="front-mark"><span class="dot"></span>Velmora</div>
  </section>
</main>
</body>
</html>
```